Entertainment Sound and Lighting company Business card

We need a professional looking business card designed for my growing entertainment sound and lighting company based in Sydney, Australia called "Kestrel Sound"

We provide technical production services (sound systems/lighting/vision) for events ranging from band gigs, weddings, corporate functions etc.

The business card needs to contain the following information:

Bartholomew Quenneville
Audio Engineer
Phone: 0478 615 702
Email: bartholomew@kestrelsound.com.au
Website: www.kestrelsound.com.au

Business logo has been attached in .ai format, please contact me if you need me to provide other files.

Target Market(s)

We need a business card that reflects our modern and professional company but still looks professional to appeal to our corporate clients.
We have a very broad target market spanning from bands needing PA systems for their gigs (18-30yrs) to event companies needing sound and lighting for weddings and other functions.

Industry/Entity Type

Business

Requirements
Must have
• Needs to include the logo that is attached of course, and the colour scheme.
Nice to have
• - Double sided

```html
<!DOCTYPE html>
<html lang="en">
<head>
<meta charset="utf-8">
<title>Kestrel Sound — Business Card</title>
<link rel="stylesheet" href="https://fonts.googleapis.com/css2?family=Montserrat:wght@400;500;600;700&display=swap">
<style>
  :root {
    --page: #ffffff;
    --ink-label: #111111;
    --card-border: #b9b9b9;
    --divider: #c9c9c9;
    --brand-blue: #1480dc;
    --brand-mid: #1d8fe6;
    --brand-cyan: #5fd3ef;
    --back-fill: #0b7ddc;
    --white: #ffffff;
  }
  * { margin: 0; padding: 0; box-sizing: border-box; }
  html, body {
    width: 1200px;
    height: 900px;
    overflow: hidden;
    background: var(--page);
    font-family: "Montserrat", sans-serif;
  }
  .sheet {
    position: relative;
    width: 1200px;
    height: 900px;
  }
  .side-label {
    position: absolute;
    left: 106px;
    font-size: 14px;
    font-weight: 700;
    letter-spacing: 0.38em;
    color: var(--ink-label);
  }
  .side-label--front { top: 191px; }
  .side-label--back { top: 681px; }

  .card {
    position: absolute;
    left: 354px;
    width: 738px;
    height: 316px;
  }
  .card--front {
    top: 42px;
    border: 2px solid var(--card-border);
    background: var(--white);
  }
  .card--back {
    top: 532px;
    height: 318px;
    background: var(--back-fill);
    display: flex;
    align-items: center;
    justify-content: center;
  }

  .brand {
    position: absolute;
    left: 0;
    top: 0;
    width: 306px;
    height: 100%;
    display: flex;
    align-items: center;
    justify-content: center;
    gap: 12px;
  }
  .brand-mark {
    width: 16px;
    height: 16px;
    border-radius: 50%;
    background: var(--brand-mid);
  }
  .brand-name {
    font-size: 30px;
    font-weight: 700;
    color: var(--brand-mid);
    letter-spacing: -0.01em;
  }

  .divider {
    position: absolute;
    left: 306px;
    top: 28px;
    width: 2px;
    height: 258px;
    background: var(--divider);
  }

  .contact {
    position: absolute;
    left: 336px;
    top: 70px;
    color: var(--brand-blue);
  }
  .contact-name {
    font-size: 25px;
    font-weight: 600;
    line-height: 1;
    margin-bottom: 14px;
  }
  .contact-role {
    font-size: 20px;
    font-weight: 400;
    color: var(--brand-cyan);
    line-height: 1;
    margin-bottom: 18px;
  }
  .contact-line {
    font-size: 17px;
    font-weight: 500;
    line-height: 1;
    margin-bottom: 19px;
    white-space: nowrap;
  }

  .back-name {
    font-size: 44px;
    font-weight: 700;
    color: var(--white);
    letter-spacing: -0.01em;
  }
</style>
</head>
<body>
  <main class="sheet">
    <span class="side-label side-label--front">FRONT</span>
    <section class="card card--front" aria-label="Business card front">
      <div class="brand">
        <span class="brand-mark"></span>
        <span class="brand-name">Kestrel Sound</span>
      </div>
      <div class="divider"></div>
      <div class="contact">
        <p class="contact-name">Bartholomew Quenneville</p>
        <p class="contact-role">Audio Engineer</p>
        <p class="contact-line">Phone: 0478 615 702</p>
        <p class="contact-line">Email: bartholomew@kestrelsound.com.au</p>
        <p class="contact-line">Website: www.kestrelsound.com.au</p>
      </div>
    </section>

    <span class="side-label side-label--back">BACK</span>
    <section class="card card--back" aria-label="Business card back">
      <span class="back-name">Kestrel Sound</span>
    </section>
  </main>
</body>
</html>
```